Business Card Design Project

Brenton
Sales Manager

38750 Harlow Ave, Suite 415
Tustin, CA 92780

Tel: 714-382-5061
Fax: 877-524-3917
E-mail: brenton@lumobravo.com

Target Market(s)

We are the distributor and wholesaler, the business card design want to show we are a strong company.

Industry/Entity Type

Business

Colors

Designer to choose colors to be used in the design.

```html
<!DOCTYPE html>
<html lang="en">
<head>
<meta charset="utf-8">
<title>Lumobravo Business Card</title>
<link rel="stylesheet" href="https://fonts.googleapis.com/css2?family=Open+Sans:wght@400;600&family=PT+Serif&display=swap">
<style>
  :root {
    --page: #ececec;
    --card: #ffffff;
    --red: #f3321d;
    --red-deep: #ea2415;
    --orange: #ff6a1f;
    --band: #ff7a26;
    --brand: #f2401c;
    --ink-light: #ffe9e2;
    --shadow: rgba(0,0,0,0.18);
  }
  html, body {
    margin: 0;
    width: 1200px;
    height: 1000px;
    overflow: hidden;
    background: var(--page);
  }
  .canvas {
    position: relative;
    width: 1200px;
    height: 1000px;
  }
  .card {
    position: absolute;
    left: 250px;
    width: 700px;
    height: 400px;
    background: var(--card);
    box-shadow: 0 6px 18px var(--shadow);
    overflow: hidden;
  }
  .card--info { top: 70px; display: flex; }
  .card--front { top: 530px; display: flex; align-items: center; justify-content: center; }

  .card__mark-side {
    width: 45%;
    display: flex;
    align-items: center;
    justify-content: center;
  }
  .card__details {
    position: relative;
    width: 55%;
    background: linear-gradient(135deg, var(--orange) 0%, var(--red) 45%, var(--red-deep) 100%);
    border-left: 6px solid var(--band);
    box-sizing: border-box;
  }
  .card__band {
    position: absolute;
    left: 0;
    right: 0;
    top: 58px;
    height: 22px;
    background: var(--band);
    opacity: 0.85;
  }
  .holder {
    position: absolute;
    left: 60px;
    top: 40px;
    font-family: "PT Serif", Georgia, serif;
    color: var(--ink-light);
  }
  .holder__name { font-size: 26px; line-height: 30px; margin: 0; }
  .holder__role { font-size: 18px; line-height: 22px; margin: 4px 0 0; }
  .contact {
    position: absolute;
    left: 60px;
    top: 170px;
    font-family: "Open Sans", Arial, sans-serif;
    font-size: 15px;
    line-height: 20px;
    color: #ffffff;
    margin: 0;
  }
  .contact p { margin: 0; white-space: nowrap; }
  .contact .gap { margin-top: 20px; }

  .brand {
    display: flex;
    align-items: center;
    gap: 12px;
    font-family: "Open Sans", Arial, sans-serif;
    font-weight: 600;
    color: var(--brand);
  }
  .brand__dot {
    border-radius: 50%;
    background: var(--brand);
  }
  .brand--small { font-size: 28px; }
  .brand--small .brand__dot { width: 22px; height: 22px; }
  .brand--large { font-size: 40px; }
  .brand--large .brand__dot { width: 30px; height: 30px; }
</style>
</head>
<body>
<main class="canvas">
  <section class="card card--info">
    <div class="card__mark-side">
      <div class="brand brand--small"><span class="brand__dot"></span>Lumobravo</div>
    </div>
    <div class="card__details">
      <div class="card__band"></div>
      <div class="holder">
        <p class="holder__name">Brenton</p>
        <p class="holder__role">Sales Manager</p>
      </div>
      <div class="contact">
        <p>38750 Harlow Ave, Suite 415</p>
        <p>Tustin, CA 92780</p>
        <p class="gap">Tel: 714-382-5061</p>
        <p>Fax: 877-524-3917</p>
        <p>E-mail: brenton@lumobravo.com</p>
      </div>
    </div>
  </section>

  <section class="card card--front">
    <div class="brand brand--large"><span class="brand__dot"></span>Lumobravo</div>
  </section>
</main>
</body>
</html>
```